Current state of Man's Soul Christian view

I would like an improvement of my design or a reimagining of my design to help people visualize what happens to the soul after we die. The second picture "screenshot 2023" is not my design but gives another idea.

For further information, there are 4 "time" frames that could be sectioned off. Eden is one time. Then adam rebellion and pre messiah earth (with hades/ Sheol). The third time frame is Messiah death, resurrection with the current state of earth. The 4th time frame is the "heavenly realm" which is across all 3 times and is unchanged.

For color ideas, please see my website www.lanternpathnotes.org which has my color theme. But the death of Messiah I would like in some type of red as well as the death of believers.

My goal is something simple, engaging, and easy to understand. If you have any questions please lmk.
Thank you for considering my project.

```html
<!DOCTYPE html>
<html lang="en">
<head>
<meta charset="utf-8">
<title>What Happens to Your Soul After You Die?</title>
<link href="https://fonts.googleapis.com/css2?family=Poppins:wght@400;600;700;800&family=Oswald:wght@500;600&family=Creepster&display=swap" rel="stylesheet">
<style>
  :root {
    --page: #3f444b;
    --sea-top: #bcd6e8;
    --sea-mid: #4fd0e4;
    --sea-deep: #1fb6d2;
    --ink: #111111;
    --royal: #2a22d6;
    --royal-dark: #1d1a8a;
    --label-blue: #3a4fd8;
    --violet: #a56ce0;
    --violet-deep: #4b2a7a;
    --blood: #d01818;
    --blood-dark: #8e0d0d;
    --rust: #a8322a;
    --steel: #3f86b3;
    --white: #ffffff;
    --sheol: #c0141c;
  }
  * { margin: 0; padding: 0; box-sizing: border-box; }
  html, body { width: 868px; height: 1200px; overflow: hidden; background: var(--page); }
  .canvas { position: relative; width: 868px; height: 1200px; }
  .poster { position: absolute; left: 0; top: 306px; width: 868px; height: 587px; box-shadow: 0 10px 24px rgba(0,0,0,.45); }
  .poster svg { display: block; }
  .title-light { font: 400 28px "Poppins", sans-serif; fill: var(--ink); }
  .title-bold { font: 700 26px "Poppins", sans-serif; fill: var(--ink); }
  .title-big { font: 800 40px "Poppins", sans-serif; fill: var(--royal); }
  .heaven { font: 800 36px "Poppins", sans-serif; fill: var(--royal); letter-spacing: 4px; }
  .heaven-sup { font: 800 18px "Poppins", sans-serif; fill: var(--royal); }
  .heaven-sub { font: 600 10px "Poppins", sans-serif; fill: var(--white); letter-spacing: 5.4px; }
  .label-rust { font: 700 12px "Poppins", sans-serif; fill: var(--rust); }
  .label-steel { font: 700 12px "Poppins", sans-serif; fill: var(--steel); }
  .label-blue { font: 700 12px "Poppins", sans-serif; fill: var(--label-blue); }
  .eden { font: 700 15px "Poppins", sans-serif; fill: var(--royal); }
  .death { font: 800 32px "Poppins", sans-serif; fill: var(--ink); }
  .bar-text { font: 600 10px "Poppins", sans-serif; fill: var(--white); letter-spacing: 1px; }
  .bar-thin { font: 400 11px "Poppins", sans-serif; fill: var(--white); }
  .bar-small { font: 600 9px "Poppins", sans-serif; fill: var(--white); }
  .bar-cond { font: 600 14px "Oswald", sans-serif; fill: var(--white); }
  .bar-cond-lg { font: 500 17px "Oswald", sans-serif; fill: var(--white); }
  .tag { font: 400 6.5px "Poppins", sans-serif; fill: var(--ink); }
  .realm { font: 700 11px "Poppins", sans-serif; fill: var(--white); }
  .sheol { font: 400 28px "Creepster", sans-serif; fill: var(--sheol); }
</style>
</head>
<body>
<main class="canvas">
  <section class="poster">
    <svg width="868" height="587" viewBox="0 0 868 587" xmlns="http://www.w3.org/2000/svg">
      <defs>
        <linearGradient id="sea" x1="0" y1="0" x2="0" y2="1">
          <stop offset="0" stop-color="#bcd6e8"/>
          <stop offset=".3" stop-color="#4fd0e4"/>
          <stop offset="1" stop-color="#1fb6d2"/>
        </linearGradient>
        <radialGradient id="sun" cx=".5" cy="0" r=".5">
          <stop offset="0" stop-color="#fffbe8"/>
          <stop offset="1" stop-color="#fffbe8" stop-opacity="0"/>
        </radialGradient>
        <linearGradient id="beam" x1="0" y1="0" x2="0" y2="1">
          <stop offset="0" stop-color="#ffffff"/>
          <stop offset="1" stop-color="#ffffff" stop-opacity=".35"/>
        </linearGradient>
        <radialGradient id="earth-blue" cx=".4" cy=".4" r=".6">
          <stop offset="0" stop-color="#5fb0d8"/><stop offset=".6" stop-color="#2c6e8e"/><stop offset="1" stop-color="#0f2f45"/>
        </radialGradient>
        <radialGradient id="earth-red" cx=".4" cy=".4" r=".6">
          <stop offset="0" stop-color="#d2643a"/><stop offset=".6" stop-color="#8a2e1c"/><stop offset="1" stop-color="#2e2a3a"/>
        </radialGradient>
        <linearGradient id="realm" x1="0" y1="0" x2="0" y2="1">
          <stop offset="0" stop-color="#e8eef4"/><stop offset=".5" stop-color="#8c9aa8"/>
          <stop offset=".52" stop-color="#c0542a"/><stop offset="1" stop-color="#5a1a0e"/>
        </linearGradient>
        <radialGradient id="eden" cx=".5" cy=".5" r=".5">
          <stop offset="0" stop-color="#8fd36a"/><stop offset="1" stop-color="#2f7a2a"/>
        </radialGradient>
        <linearGradient id="purple-bar" x1="0" y1="0" x2="0" y2="1">
          <stop offset="0" stop-color="#2b2a8f"/><stop offset="1" stop-color="#4b2a7a"/>
        </linearGradient>
      </defs>

      <!-- sky and sea backdrop -->
      <rect width="868" height="587" fill="url(#sea)" role="img" aria-label="Photograph of sunlit clouds over a turquoise sea"/>
      <ellipse cx="434" cy="0" rx="260" ry="180" fill="url(#sun)"/>

      <!-- title -->
      <text class="title-light" x="47" y="80">What happens</text>
      <text class="title-bold" x="47" y="112">to your soul, After</text>
      <text class="title-big" x="47" y="152">You Die?</text>

      <!-- heaven heading -->
      <text class="heaven" x="366" y="108">3<tspan class="heaven-sup" dy="-14" dx="4">RD</tspan><tspan dy="14" dx="12">HEAVEN</tspan></text>
      <rect x="368" y="113" width="274" height="13" rx="3" fill="var(--steel)"/>
      <text class="heaven-sub" x="380" y="123">GOD'S HEAVENLY EARTH</text>

      <!-- resurrection beam and arrow -->
      <rect x="478" y="180" width="56" height="407" fill="url(#beam)"/>
      <path d="M467 182 L505 128 L544 182 L526 182 L526 200 L486 200 L486 182 Z" fill="var(--white)" stroke="#6a6ad8" stroke-width="1.5"/>
      <path d="M486 200 L526 200 L526 587 L486 587 Z" fill="#ffffff" fill-opacity=".7"/>
      <rect x="478" y="192" width="60" height="246" rx="14" fill="var(--ink)" role="img" aria-label="Silhouette of a risen figure with arms raised"/>
      <text class="bar-cond-lg" transform="translate(513 425) rotate(-90)">MESSIAH RESURRECTION</text>

      <!-- messiah death bar -->
      <rect x="372" y="208" width="96" height="26" rx="3" fill="var(--blood-dark)" fill-opacity=".85" role="img" aria-label="Illustration of a figure on a cross"/>
      <path d="M404 234 L435 234 L435 426 L384 426 L384 436 L358 414 L384 392 L384 402 L404 402 Z" fill="var(--blood)"/>
      <text class="bar-cond" transform="translate(425 396) rotate(-90)">MESSIAH DEATH</text>

      <!-- Holy Spirit descends -->
      <path d="M553 131 L572 131 L572 277 L586 277 L586 268 L602 284 L586 300 L586 291 L553 291 Z" fill="var(--violet)"/>
      <text class="bar-small" transform="translate(567 280) rotate(-90)">HOLYSPIRIT DESCENDS</text>

      <!-- believers in messiah -->
      <path d="M813 102 L813 314 L776 314 L776 137 L690 137 L690 148 L656 118 L690 88 L690 102 Z" fill="var(--royal-dark)"/>
      <text class="bar-text" transform="translate(799 302) rotate(-90)">BELIEVERS IN MESSIAH</text>

      <!-- non-believers -->
      <path d="M792 360 L823 360 L823 490 L740 490 L740 500 L717 472 L740 446 L740 456 L792 456 Z" fill="var(--blood)"/>
      <text class="bar-small" transform="translate(811 482) rotate(-90)">NON- BELIEVERS</text>
      <text class="death" x="696" y="350">DEATH</text>

      <!-- current fallen earth -->
      <text class="label-blue" x="604" y="200">CURRENT</text>
      <text class="label-blue" x="590" y="214">FALLEN EARTH</text>
      <circle cx="643" cy="278" r="61" fill="url(#earth-blue)" role="img" aria-label="Photograph of the earth, the current fallen world"/>

      <!-- right Hades / Sheol -->
      <circle cx="644" cy="431" r="81" fill="url(#realm)" role="img" aria-label="Image of Hades split into paradise above and torment below"/>
      <text class="realm" x="644" y="436" text-anchor="middle">PARADISE</text>
      <text class="realm" x="644" y="497" text-anchor="middle">TORMENT</text>
      <text class="sheol" x="566" y="556" textLength="156" lengthAdjust="spacingAndGlyphs">HADES / SHEOL</text>

      <!-- pre-messiah fallen earth -->
      <text class="label-rust" x="265" y="189">PRE-MESSIAH</text>
      <text class="label-rust" x="265" y="204">FALLEN EARTH</text>
      <circle cx="318" cy="260" r="56" fill="url(#earth-red)" role="img" aria-label="Photograph of the earth half scorched, the fallen world before the Messiah"/>

      <!-- left Hades / Sheol -->
      <circle cx="313" cy="440" r="68" fill="url(#realm)" role="img" aria-label="Image of Hades split into paradise above and torment below"/>
      <text class="realm" x="313" y="431" text-anchor="middle">PARADISE</text>
      <text class="realm" x="313" y="487" text-anchor="middle">TORMENT</text>
      <text class="sheol" x="229" y="556" textLength="157" lengthAdjust="spacingAndGlyphs">HADES / SHEOL</text>

      <!-- narrow gate -->
      <rect x="241" y="330" width="66" height="14" fill="var(--white)" fill-opacity=".9"/>
      <text class="tag" x="246" y="340">NARROW GATE</text>
      <path d="M298 344 L298 360 L293 360 L301 370 L309 360 L304 360 L304 344 Z" fill="#cfeaf6"/>

      <!-- first man's rebellion and Eden -->
      <circle cx="162" cy="205" r="9" fill="var(--blood)"/>
      <text class="label-steel" x="211" y="204" text-anchor="middle">FIRST MAN</text>
      <text class="label-steel" x="211" y="218" text-anchor="middle">REBELLION</text>
      <text class="death" transform="translate(233 352) rotate(-90)">DEATH</text>
      <path d="M207 358 L234 358 L234 460 L265 460 L265 452 L284 466 L265 480 L265 473 L207 473 Z" fill="url(#purple-bar)"/>
      <text class="bar-thin" transform="translate(226 453) rotate(-90)">WIDE GATE</text>
      <text class="eden" x="98" y="274">EDEN</text>
      <circle cx="122" cy="350" r="67" fill="url(#eden)" stroke="var(--royal-dark)" stroke-width="3" role="img" aria-label="Illustration of a green garden with trees, the Garden of Eden"/>
    </svg>
  </section>
</main>
</body>
</html>
```